Flaschenetiketten-Design in rechteckiger Grundform für Biermanufaktur
Der Kontakt war sehr professionell und angenehm. Wir wurden hilfreich beraten. Auf unser Feedback haben wir in kurzer Zeit jeweils neue Entwürfe erhalten. Die Zusammenarbeit und der Service war deutlich über unseren Vorstellungen. Wir können KorvaneDeck nur weiterempfehlen!
Zielgruppe
Wir repräsentieren eine Bier-Manufaktur in der Gründungsphase und sind auf der Suche nach einem Designvorschlag für die Flaschenetiketten.
Unsere Zielgruppe sind Liebhaber, die auf der Suche nach dem Speziellen und Lokalen sind. Der Biergenuss abseits des Massenmarktes soll im Entwurf sichtbar/transportiert werden. Die Bier-Manufaktur steht zeitgleich für Trend-Kreationen mit bodenständigem Ursprung.
Aufgabenstellung
Die Herkunft der Gründer Familie aus dem Schweizer Kanton Simplon soll im Vordergrund stehen, hierzu bitte das Familienwappen / einzelne Elemente siehe Dateiupload berücksichtigen.
Das Etikett soll eine rechteckige Grundform haben.
Folgende Angaben sollen sich im Etikett wiederfinden:
- Biersorte: 'Lager' (zukünftig soll es möglich sein, Biersorte auf dem Etikett zu wechseln)
Brand: 'Mostly Grafun'
'Biermanufaktur Walliser Ursprungs'
Die Schrift soll klar und nicht zu verspielt sein.

```html
<!DOCTYPE html>
<html lang="de">
<head>
<meta charset="utf-8">
<title>Mostly Grafun – Lagerbier Etikett</title>
<link href="https://fonts.googleapis.com/css2?family=Montserrat:wght@500;600&display=swap" rel="stylesheet">
<style>
  :root {
    --page: #ffffff;
    --frame: #c4c4c4;
    --panel-top: #23292c;
    --panel-bottom: #262626;
    --scene-a: #2c3236;
    --scene-b: #3a3a37;
    --band: #c2c2c2;
    --band-line: #5a5a5a;
    --ink-light: #ffffff;
    --ink-dark: #2b2b2b;
  }
  * { box-sizing: border-box; margin: 0; padding: 0; }
  html, body { width: 844px; height: 1200px; overflow: hidden; background: var(--page); }
  .canvas { position: relative; width: 844px; height: 1200px; }
  .label {
    position: absolute; left: 142px; top: 290px; width: 560px; height: 621px;
    background: var(--frame); padding: 10px;
    box-shadow: 8px 10px 14px rgba(0,0,0,0.35);
  }
  .label-panel {
    position: relative; width: 100%; height: 100%; overflow: hidden;
    background: linear-gradient(180deg, var(--panel-top), var(--panel-bottom));
    font-family: "Montserrat", sans-serif;
  }
  .scene {
    position: absolute; left: 0; top: 0; width: 100%; height: 428px;
    background: radial-gradient(ellipse at 40% 70%, var(--scene-b) 0%, var(--scene-a) 55%, var(--panel-top) 100%);
    opacity: 0.8;
  }
  .brand {
    position: absolute; left: 0; right: 0; top: 160px;
    text-align: center; color: var(--ink-light);
    font-weight: 600; font-size: 64px; line-height: 78px; letter-spacing: 3px;
  }
  .band {
    position: absolute; left: 0; right: 0; top: 438px; height: 66px;
    background: var(--band);
    border-top: 2px solid var(--band-line); border-bottom: 2px solid var(--band-line);
    outline: 3px solid var(--band); outline-offset: 0;
  }
  .band-rule { position: absolute; left: 0; right: 0; height: 2px; background: var(--band); }
  .band-rule.top { top: 432px; }
  .band-rule.bottom { top: 508px; }
  .band-text {
    position: absolute; top: 50%; transform: translateY(-50%);
    color: var(--ink-dark); font-weight: 500; font-size: 13px; letter-spacing: 1.6px;
  }
  .band-text.left { left: 18px; }
  .band-text.right { right: 0; }
  .crest {
    position: absolute; left: 50%; top: 422px; width: 110px; height: 110px;
    transform: translateX(-50%);
    background: var(--band); border: 2px solid var(--band-line);
    display: flex; align-items: center; justify-content: center; text-align: center;
    color: var(--ink-dark); font-weight: 500; font-size: 12px; line-height: 16px; letter-spacing: 1px;
  }
  .variety {
    position: absolute; left: 0; right: 0; top: 560px; text-align: center;
    color: var(--ink-light); font-weight: 500; font-size: 17px; letter-spacing: 2.5px;
  }
</style>
</head>
<body>
<div class="canvas">
  <div class="label">
    <div class="label-panel">
      <div class="scene" role="img" aria-label="Dunkles Foto einer verschneiten Berglandschaft mit Steinmonument"></div>
      <h1 class="brand">MOSTLY<br>GRAFUN</h1>
      <div class="band-rule top"></div>
      <div class="band">
        <span class="band-text left">BIERMANUFAKTUR</span>
        <span class="band-text right">WALLISER URSPRUNGS</span>
      </div>
      <div class="band-rule bottom"></div>
      <div class="crest">MOSTLY<br>GRAFUN</div>
      <p class="variety">- LAGERBIER -</p>
    </div>
  </div>
</div>
</body>
</html>
```